Project Meridel PowerPoint Design

This is a PPT design for Power & Utilities company who are in the process of a technology upgrade for their Finance department. We are looking to develop a branded PPT for Project Meridel (specifically MERIDEL). Why does Meridel resonate? "The Earth is pointed almost directly at Meridel. During the course of the night,
Meridel does not rise or set, but remains in nearly the same spot above the
northern horizon year- round while the other stars circle around it."
Meridel represents the guiding principles that manage, monitor and
control the organizations financials.

Target Market(s)

Finance stakeholders impacted by technology enhancement

Font styles to use
Serif
Other font styles liked:
• Arial

Colors
0054AA
0677BA
7BADD7
CADEEF
E8F1F8

Requirements
Must have
• Various slide layout ( Cover slide, content slide, divider, etc). Attached is the logo and corporate colors
Nice to have
• Over the top creativity

```html
<!DOCTYPE html>
<html lang="en">
<head>
<meta charset="utf-8">
<title>Project Meridel – Presentation Slides</title>
<link href="https://fonts.googleapis.com/css2?family=Source+Serif+4:opsz,wght@8..60,400;8..60,600;8..60,700&display=swap" rel="stylesheet">
<style>
:root{
  --canvas:#d9d9d9;
  --primary:#0054aa;
  --blue:#0677ba;
  --sky:#7badd7;
  --pale:#cadeef;
  --ice:#e8f1f8;
  --white:#ffffff;
  --ink:#2b2f36;
  --muted:#6f7680;
  --grey:#9a9ea4;
  --row:#e8f1f8;
}
*{box-sizing:border-box;margin:0;padding:0}
html,body{width:1200px;height:4724px;overflow:hidden}
body{background:var(--canvas);font-family:"Source Serif 4",Georgia,serif;color:var(--ink);position:relative}
.slide{position:absolute;left:110px;width:982px;height:551px;background:var(--white);overflow:hidden}
.header-band{position:absolute;left:0;top:0;width:982px;height:180px}
.slide-title{position:absolute;left:60px;top:36px;color:var(--white);font-weight:700;font-size:30px;letter-spacing:.3px}
.brand{position:absolute;font-weight:700;letter-spacing:2px;display:flex;align-items:center;gap:8px;white-space:nowrap}
.brand .dot{width:10px;height:10px;border-radius:50%;background:currentColor}
.brand-header{right:80px;top:42px;color:var(--white);font-size:26px}
.photo{position:absolute}
/* cover */
.cover-title{position:absolute;left:57px;top:448px;font-size:32px;font-weight:700;color:var(--primary)}
.cover-sub{position:absolute;left:60px;top:497px;font-size:12px;color:var(--muted)}
.brand-cover-top{left:58px;top:145px;color:var(--white);font-size:34px}
.brand-cover-foot{right:60px;top:478px;color:var(--primary);font-size:26px}
/* bullets */
.ticks{position:absolute;list-style:none}
.ticks li{position:relative;padding-left:26px;font-size:11.5px;line-height:19px;color:#555;margin-bottom:9px}
.ticks li::before{content:"";position:absolute;left:2px;top:4px;width:11px;height:11px;border-radius:50%;background:var(--primary)}
.ticks li::after{content:"";position:absolute;left:5px;top:6px;width:5px;height:3px;border-left:1.5px solid #fff;border-bottom:1.5px solid #fff;transform:rotate(-45deg)}
/* vision */
.statement{position:absolute;left:60px;display:flex;gap:20px}
.statement .badge{flex:none;width:76px;height:76px;border-radius:50%;display:flex;align-items:center;justify-content:center}
.statement h3{font-size:14px;font-weight:700;margin:2px 0 10px}
.statement p{font-size:11.5px;line-height:19px;color:#666;width:290px}
/* team */
.team-card{position:absolute;top:171px;width:208px;height:306px;border:1.5px solid var(--pale);border-radius:8px;text-align:center}
.avatar{width:88px;height:88px;border-radius:50%;margin:24px auto 20px}
.team-card h4{font-size:10px;font-weight:700;color:#222}
.team-card .role{font-size:9.5px;font-weight:700;margin:6px 0 10px}
.team-card p{font-size:9.5px;line-height:14px;color:#666;padding:0 14px}
.social{display:flex;justify-content:center;gap:4px;margin-top:12px}
.social span{width:19px;height:19px;border:1.5px solid var(--primary);border-radius:50%}
/* table */
.icon-rail{position:absolute;left:116px;top:228px;width:60px;height:262px;background:var(--grey);display:flex;flex-direction:column;justify-content:space-around;align-items:center}
.col-head{position:absolute;top:198px;width:211px;height:33px;color:#fff;font-size:12px;font-weight:600;display:flex;align-items:center;justify-content:center}
.col-head.grey{background:var(--grey)}
.col-head.accent{background:var(--primary)}
.col-head.accent::after{content:"";position:absolute;bottom:-8px;left:50%;margin-left:-8px;border-left:8px solid transparent;border-right:8px solid transparent;border-top:8px solid var(--primary)}
.t-row{position:absolute;left:176px;width:688px;height:46px;display:grid;grid-template-columns:44px 211px 5px 211px 5px 211px;align-items:center;font-size:10.5px;color:#444;text-align:center}
.t-row.shade{background:var(--row)}
.t-row span:nth-child(1){grid-column:2}
.t-row span:nth-child(2){grid-column:4}
.t-row span:nth-child(3){grid-column:6}
/* chart */
.chart{position:absolute;left:40px;top:160px}
/* qa */
.qa{position:absolute;display:flex;gap:14px;align-items:center}
.qa .q{flex:none;width:30px;height:30px;border-radius:50%;color:#fff;font-size:12px;font-weight:700;display:flex;align-items:center;justify-content:center;box-shadow:0 0 0 4px #e6e6e6}
.qa .q.grey{background:var(--grey)}
.qa .q.accent{background:var(--primary);box-shadow:0 0 0 4px var(--pale)}
.qa p{font-size:11px;font-weight:700;line-height:17px;color:#222;width:300px}
</style>
</head>
<body>

<!-- Cover -->
<section class="slide" style="top:187px">
  <svg width="982" height="551" viewBox="0 0 982 551">
    <path d="M0 0H982V370C900 420 760 440 620 380C470 320 330 300 180 325C90 340 30 360 0 375Z" fill="var(--primary)"/>
    <path d="M560 0C450 90 470 260 620 340C730 400 870 390 982 350V0Z" fill="var(--blue)"/>
    <path d="M640 0C560 90 570 230 680 300C770 350 890 340 982 300V0Z" fill="var(--sky)" opacity=".6"/>
  </svg>
  <svg class="photo" style="left:470px;top:0" width="512" height="330">
    <defs><linearGradient id="coverPhoto" x1="0" y1="0" x2="1" y2="1"><stop offset="0" stop-color="#b9a27a"/><stop offset=".5" stop-color="#8b8d8f"/><stop offset="1" stop-color="#4e5a6a"/></linearGradient></defs>
    <ellipse role="img" aria-label="Photo of a team working on a laptop and tablet" cx="330" cy="120" rx="230" ry="190" fill="url(#coverPhoto)"/>
  </svg>
  <div class="brand brand-cover-top"><span class="dot"></span>PROJECT MERIDEL</div>
  <h1 class="cover-title">MERIDEL PROJECT</h1>
  <p class="cover-sub">Lorem ipsum dolor sit amet, consectetur adipiscing elit, sed do eiusmod</p>
  <div class="brand brand-cover-foot"><span class="dot"></span>MERIDEL</div>
</section>

<!-- Content -->
<section class="slide" style="top:820px">
  <svg class="header-band" viewBox="0 0 982 180"><path d="M0 0H982V30C965 80 935 110 880 110H140C70 110 20 140 0 178Z" fill="var(--primary)"/></svg>
  <h2 class="slide-title">TITLE HERE</h2>
  <div class="brand brand-header"><span class="dot"></span>MERIDEL</div>
  <ul class="ticks" style="left:60px;top:165px;width:440px">
    <li>Lorem ipsum dolor sit consectetur adipiscing elit, sed do eiusmod tempor incididunt ut labore et dolore magna aliqua.</li>
    <li>Lorem ipsum dolor sit consectetur adipiscing elit, sed do eiusmod tempor incididunt ut labore et dolore magna aliqua.</li>
    <li>Lorem ipsum dolor sit consectetur adipiscing elit, sed do eiusmod tempor incididunt ut labore et dolore magna aliqua.</li>
    <li>Lorem ipsum dolor sit consectetur adipiscing elit, sed do eiusmod tempor incididunt ut labore et dolore magna aliqua.</li>
    <li>Lorem ipsum dolor sit consectetur adipiscing elit, sed do eiusmod tempor incididunt ut labore et dolore magna aliqua.</li>
    <li>Lorem ipsum dolor sit consectetur adipiscing elit, sed do eiusmod tempor incididunt ut labore et dolore magna aliqua.</li>
    <li>Lorem ipsum dolor sit consectetur adipiscing elit, sed do eiusmod tempor incididunt ut labore et dolore magna aliqua.</li>
  </ul>
  <div class="photo" role="img" aria-label="Photo of colleagues reviewing charts on a tablet" style="left:543px;top:149px;width:375px;height:352px;border-radius:0 0 50px 0;background:linear-gradient(135deg,#7a6a5c,#a8a39a 50%,#3d4e66)"></div>
</section>

<!-- Vision & mission -->
<section class="slide" style="top:1453px">
  <svg class="header-band" viewBox="0 0 982 180"><path d="M0 0H982V30C965 80 935 110 880 110H140C70 110 20 140 0 178Z" fill="var(--primary)"/></svg>
  <h2 class="slide-title">TITLE HERE</h2>
  <div class="brand brand-header"><span class="dot"></span>MERIDEL</div>
  <div class="statement" style="top:225px">
    <div class="badge" style="background:var(--primary)"><svg width="40" height="40" viewBox="0 0 40 40" fill="none" stroke="#fff" stroke-width="2.5"><circle cx="20" cy="20" r="15"/><circle cx="20" cy="20" r="9"/><circle cx="20" cy="20" r="3"/><path d="M20 20L34 6"/></svg></div>
    <div><h3>Vision</h3><p>At vero eos et accusamus et iusto dignissimos ducimus qui blanditiis praesentium voluptatum deleniti atque corrupti</p></div>
  </div>
  <div class="statement" style="top:352px">
    <div class="badge" style="background:#555"><svg width="40" height="40" viewBox="0 0 40 40" fill="none" stroke="#fff" stroke-width="2.5"><path d="M8 18L30 8L33 15L11 25Z"/><path d="M20 22L14 36M20 22L26 36M20 22V36"/></svg></div>
    <div><h3>Mission</h3><p>Sed ut perspiciatis unde omnis iste natus error sit voluptatem accusantium doloremque laudantium, totam rem aperiam, eaque ipsa quae ab illo inventore veritatis et quasi</p></div>
  </div>
  <svg class="photo" style="left:500px;top:160px" width="440" height="340">
    <defs><linearGradient id="tabletPhoto" x1="0" y1="0" x2="1" y2="1"><stop offset="0" stop-color="#2a2a2a"/><stop offset=".5" stop-color="#8a5a2a"/><stop offset="1" stop-color="#1f1f1f"/></linearGradient></defs>
    <path role="img" aria-label="Photo of a tablet showing a financial chart" d="M160 30L410 90L310 310L20 200Z" fill="url(#tabletPhoto)"/>
  </svg>
</section>

<!-- Team -->
<section class="slide" style="top:2088px">
  <svg class="header-band" viewBox="0 0 982 180"><path d="M0 0H982V30C965 80 935 110 880 110H140C70 110 20 140 0 178Z" fill="var(--primary)"/></svg>
  <h2 class="slide-title">OUR TEAM</h2>
  <div class="brand brand-header"><span class="dot"></span>MERIDEL</div>
  <div class="team-card" style="left:51px"><div class="avatar" role="img" aria-label="Portrait photo of team member" style="background:linear-gradient(#8a6a55,#c9a58a)"></div><h4>ALAN CARVER</h4><div class="role">PARTNER</div><p>Lorem ipsum dolor amet, consectetur adipiscing elit, sed eiusmod tempor incididunt ut labore et dolore magna aliqua. Ut enim ad minim veniam, quis nostrud exercitation ullamco</p><div class="social"><span></span><span></span><span></span></div></div>
  <div class="team-card" style="left:271px"><div class="avatar" role="img" aria-label="Portrait photo of team member" style="background:linear-gradient(#b88a60,#e0c4a6)"></div><h4>ALAN CARVER</h4><div class="role">PARTNER</div><p>Lorem ipsum dolor amet, consectetur adipiscing elit, sed eiusmod tempor incididunt ut labore et dolore magna aliqua. Ut enim ad minim veniam, quis nostrud exercitation ullamco</p><div class="social"><span></span><span></span><span></span></div></div>
  <div class="team-card" style="left:491px"><div class="avatar" role="img" aria-label="Portrait photo of team member" style="background:linear-gradient(#6e4a35,#c79c7e)"></div><h4>ALAN CARVER</h4><div class="role">PARTNER</div><p>Lorem ipsum dolor amet, consectetur adipiscing elit, sed eiusmod tempor incididunt ut labore et dolore magna aliqua. Ut enim ad minim veniam, quis nostrud exercitation ullamco</p><div class="social"><span></span><span></span><span></span></div></div>
  <div class="team-card" style="left:711px"><div class="avatar" role="img" aria-label="Portrait photo of team member" style="background:linear-gradient(#7a6a60,#c8aa96)"></div><h4>ALAN CARVER</h4><div class="role">PARTNER</div><p>Lorem ipsum dolor amet, consectetur adipiscing elit, sed eiusmod tempor incididunt ut labore et dolore magna aliqua. Ut enim ad minim veniam, quis nostrud exercitation ullamco</p><div class="social"><span></span><span></span><span></span></div></div>
</section>

<!-- Table -->
<section class="slide" style="top:2721px">
  <svg class="header-band" viewBox="0 0 982 180"><path d="M0 0H982V30C965 80 935 110 880 110H140C70 110 20 140 0 178Z" fill="var(--primary)"/></svg>
  <h2 class="slide-title" style="left:80px">COMMON TABLES</h2>
  <div class="brand brand-header"><span class="dot"></span>MERIDEL</div>
  <div class="col-head grey" style="left:220px">Text Here</div>
  <div class="col-head accent" style="left:436px">Text Here</div>
  <div class="col-head grey" style="left:652px">Text Here</div>
  <div class="icon-rail">
    <svg width="26" height="26" viewBox="0 0 26 26" fill="none" stroke="#fff" stroke-width="2.5"><circle cx="13" cy="13" r="10"/><path d="M13 13L18 8"/></svg>
    <svg width="26" height="26" viewBox="0 0 26 26" fill="#fff"><circle cx="15" cy="7" r="5"/><rect x="2" y="15" width="20" height="7" rx="3"/></svg>
    <svg width="26" height="26" viewBox="0 0 26 26" fill="#fff"><rect x="3" y="4" width="20" height="18" rx="2"/><rect x="6" y="9" width="14" height="2" fill="#9a9ea4"/><rect x="6" y="14" width="14" height="2" fill="#9a9ea4"/></svg>
    <svg width="26" height="26" viewBox="0 0 26 26" fill="#fff"><circle cx="13" cy="8" r="6"/><path d="M2 25C2 17 24 17 24 25Z"/></svg>
    <svg width="26" height="26" viewBox="0 0 26 26" fill="#fff"><circle cx="11" cy="11" r="9"/><circle cx="19" cy="19" r="5" stroke="#9a9ea4" stroke-width="2"/></svg>
  </div>
  <div class="t-row shade" style="top:240px"><span>Add Contents Title</span><span>Add Contents Title</span><span>Add Contents Title</span></div>
  <div class="t-row" style="top:288px"><span>Add Contents Title</span><span>Add Contents Title</span><span>Add Contents Title</span></div>
  <div class="t-row shade" style="top:334px"><span>Add Contents Title</span><span>Add Contents Title</span><span>Add Contents Title</span></div>
  <div class="t-row" style="top:380px"><span>Add Contents Title</span><span>Add Contents Title</span><span>Add Contents Title</span></div>
  <div class="t-row shade" style="top:424px"><span>Add Contents Title</span><span>Add Contents Title</span><span>Add Contents Title</span></div>
</section>

<!-- Chart -->
<section class="slide" style="top:3354px">
  <svg class="header-band" viewBox="0 0 982 180"><path d="M0 0H982V30C965 80 935 110 880 110H140C70 110 20 140 0 178Z" fill="var(--primary)"/></svg>
  <h2 class="slide-title">CHART HERE</h2>
  <div class="brand brand-header"><span class="dot"></span>MERIDEL</div>
  <svg class="chart" width="570" height="360" viewBox="0 0 570 360" font-family="Source Serif 4, Georgia, serif" font-size="10" font-weight="700">
    <g fill="#444" text-anchor="end">
      <text x="20" y="14">120</text><text x="20" y="70">100</text><text x="20" y="126">80</text><text x="20" y="182">60</text><text x="20" y="238">40</text><text x="20" y="283">20</text><text x="20" y="333">0</text>
    </g>
    <g stroke="#ddd"><path d="M40 20V330M113 20V330M186 20V330M259 20V330M332 20V330M405 20V330M478 20V330M551 20V330"/></g>
    <g fill="var(--primary)">
      <rect x="58" y="72" width="13" height="258"/><rect x="131" y="98" width="13" height="232"/><rect x="204" y="201" width="13" height="129"/><rect x="277" y="72" width="13" height="258"/><rect x="350" y="72" width="13" height="258"/><rect x="423" y="175" width="13" height="155"/><rect x="496" y="201" width="13" height="129"/>
    </g>
    <g fill="var(--sky)">
      <rect x="76" y="98" width="13" height="232"/><rect x="149" y="123" width="13" height="207"/><rect x="222" y="72" width="13" height="258"/><rect x="295" y="175" width="13" height="155"/><rect x="368" y="98" width="13" height="232"/><rect x="441" y="136" width="13" height="194"/><rect x="514" y="72" width="13" height="258"/>
    </g>
    <g fill="#333" text-anchor="middle" font-size="9">
      <text x="64" y="67">100</text><text x="83" y="93">90</text><text x="137" y="93">90</text><text x="155" y="118">80</text><text x="210" y="196">50</text><text x="228" y="67">100</text><text x="283" y="67">100</text><text x="301" y="170">60</text><text x="356" y="67">100</text><text x="374" y="93">90</text><text x="429" y="170">60</text><text x="447" y="131">75</text><text x="502" y="196">50</text><text x="520" y="67">100</text>
    </g>
    <g fill="#444" text-anchor="middle">
      <text x="76" y="348">Sun</text><text x="149" y="348">Mon</text><text x="222" y="348">Tue</text><text x="295" y="348">Wed</text><text x="368" y="348">Thu</text><text x="441" y="348">Fri</text><text x="514" y="348">Sat</text>
    </g>
  </svg>
  <ul class="ticks" style="left:648px;top:155px;width:290px">
    <li>Lorem ipsum dolor sit consectetur adipiscing elit, sed do eiusmod tempor incididunt ut labore et dolore magna aliqua.</li>
    <li>Lorem ipsum dolor sit consectetur adipiscing elit, sed do eiusmod</li>
    <li>Lorem ipsum dolor sit consectetur adipiscing elit, sed do eiusmod tempor incididunt ut labore et dolore magna aliqua.</li>
    <li>Lorem ipsum dolor sit consectetur adipiscing elit, sed do eiusmod</li>
    <li>Lorem ipsum dolor sit consectetur adipiscing elit, sed do eiusmod tempor incididunt ut labore et dolore magna aliqua.</li>
    <li>Lorem ipsum dolor sit consectetur adipiscing elit, sed do eiusmod</li>
  </ul>
</section>

<!-- Q&A -->
<section class="slide" style="top:3987px">
  <svg class="header-band" viewBox="0 0 982 180"><path d="M0 0H982V30C965 80 935 110 880 110H140C70 110 20 140 0 178Z" fill="var(--primary)"/></svg>
  <h2 class="slide-title">QUESTIONS &amp; ANSWER</h2>
  <div class="brand brand-header"><span class="dot"></span>MERIDEL</div>
  <div class="qa" style="left:95px;top:163px"><span class="q grey">Q</span><p>Lorem ipsum dolor sit amet, consectetur adipiscing elit, sed do eiusmod tempor incididunt</p></div>
  <div class="qa" style="left:95px;top:216px"><span class="q accent">Q</span><p>Lorem ipsum dolor sit amet, consectetur adipiscing elit, sed do eiusmod tempor incididunt</p></div>
  <div class="qa" style="left:95px;top:293px"><span class="q grey">Q</span><p>Lorem ipsum dolor sit amet, consectetur adipiscing elit, sed do eiusmod tempor incididunt</p></div>
  <div class="qa" style="left:95px;top:346px"><span class="q accent">Q</span><p>Lorem ipsum dolor sit amet, consectetur adipiscing elit, sed do eiusmod tempor incididunt</p></div>
  <div class="qa" style="left:95px;top:424px"><span class="q grey">Q</span><p>Lorem ipsum dolor sit amet, consectetur adipiscing elit, sed do eiusmod tempor incididunt</p></div>
  <div class="qa" style="left:95px;top:477px"><span class="q accent">Q</span><p>Lorem ipsum dolor sit amet, consectetur adipiscing elit, sed do eiusmod tempor incididunt</p></div>
  <div class="qa" style="left:526px;top:163px"><span class="q grey">Q</span><p>Lorem ipsum dolor sit amet, consectetur adipiscing elit, sed do eiusmod tempor incididunt</p></div>
  <div class="qa" style="left:526px;top:216px"><span class="q accent">Q</span><p>Lorem ipsum dolor sit amet, consectetur adipiscing elit, sed do eiusmod tempor incididunt</p></div>
  <div class="qa" style="left:526px;top:293px"><span class="q grey">Q</span><p>Lorem ipsum dolor sit amet, consectetur adipiscing elit, sed do eiusmod tempor incididunt</p></div>
  <div class="qa" style="left:526px;top:346px"><span class="q accent">Q</span><p>Lorem ipsum dolor sit amet, consectetur adipiscing elit, sed do eiusmod tempor incididunt</p></div>
  <div class="qa" style="left:526px;top:424px"><span class="q grey">Q</span><p>Lorem ipsum dolor sit amet, consectetur adipiscing elit, sed do eiusmod tempor incididunt</p></div>
  <div class="qa" style="left:526px;top:477px"><span class="q accent">Q</span><p>Lorem ipsum dolor sit amet, consectetur adipiscing elit, sed do eiusmod tempor incididunt</p></div>
</section>

</body>
</html>
```